Political themed graphic for contemporary church sermon series

Contemporary church in California need a graphic design for a sermon series. The sermon series will be focused on the upcoming presidential election. The sermon series is titled for the question "who will be the next president":

Title: 45
Subtitle: Who will it be / Does it matter

The design should use red, white and blue and should possibly have the amber lodge in the graphic somewhere. Maybe like a watermark or something to that effect.

Target Market(s)

Contemporary design,

Industry/Entity Type

Church

Font styles to use
Serif
Sans Serif

Colors
0555a3
ec1f27
ffffff

Requirements
Must have
• Political theme, red, white and blue (contemporary color palette). Amber lodge screened back in the design somewhere.
• the title large: 45
• and subtitle: Who will it be | Does it matter
Should not have
• I'm not looking for cheesy graphics with elephant and a donkey.

```html
<!DOCTYPE html>
<html lang="en">
<head>
<meta charset="utf-8">
<title>45 — Sermon Series</title>
<link rel="stylesheet" href="https://fonts.googleapis.com/css2?family=Bebas+Neue&family=Montserrat:wght@600&display=swap">
<style>
  :root {
    --blue-top: #3557a6;
    --blue-bottom: #283a85;
    --red: #ec1f27;
    --white: #ffffff;
    --shadow: #231f20;
    --lodge-light: #f4f5fa;
    --lodge-shade: #b3b7cf;
  }
  html, body {
    margin: 0;
    padding: 0;
    overflow: hidden;
    background: var(--white);
  }
  .series-card {
    position: relative;
    width: 1200px;
    height: 778px;
    overflow: hidden;
    background: linear-gradient(180deg, var(--blue-top) 0%, var(--blue-bottom) 75%);
  }
  .series-title {
    position: absolute;
    left: 200px;
    top: -38px;
    margin: 0;
    font-family: "Montserrat", sans-serif;
    font-weight: 600;
    font-size: 530px;
    line-height: 1;
    letter-spacing: 10px;
    color: var(--white);
    text-shadow: 26px 8px 0 var(--shadow);
  }
  .lodge-illustration {
    position: absolute;
    left: 338px;
    top: 320px;
    width: 526px;
    height: 270px;
    background: linear-gradient(180deg, var(--lodge-light) 0%, var(--lodge-shade) 100%);
  }
  .subtitle-band {
    position: absolute;
    left: 0;
    top: 584px;
    width: 1200px;
    height: 194px;
    background: var(--red);
  }
  .subtitle {
    position: absolute;
    top: 44px;
    margin: 0;
    font-family: "Bebas Neue", sans-serif;
    font-weight: 400;
    font-size: 86px;
    line-height: 1;
    letter-spacing: 2px;
    color: var(--white);
    white-space: nowrap;
  }
  .subtitle--question { left: 108px; }
  .subtitle--answer { left: 642px; }
  .subtitle-divider {
    position: absolute;
    left: 594px;
    top: 32px;
    width: 4px;
    height: 132px;
    background: var(--white);
  }
</style>
</head>
<body>
  <main class="series-card">
    <h1 class="series-title">45</h1>
    <div class="lodge-illustration" role="img" aria-label="Illustration of the Amber Lodge, a columned mansion with a flag on its roof, screened back in white and lavender"></div>
    <section class="subtitle-band">
      <p class="subtitle subtitle--question">Who will it be</p>
      <span class="subtitle-divider" aria-hidden="true"></span>
      <p class="subtitle subtitle--answer">Does it matter</p>
    </section>
  </main>
</body>
</html>
```